Coffee bag stamp design for new coffee brand

Stamp design that will be used like a label on a coffee package.
It must be a vector that can be produced as a stamp. Coffee bag is from brown craft paper. I upload image of this bag. Size of design is 80mm x 140mm.
I also uploaded two pictures for inspiration, but I will also appreciate new ideas.

Target Market(s)

Coffee lovers, who love to try new coffee. Also hipsters.

Colors

Designer to choose only greyscale colors for use in the design.

Requirements
Must have
• Some information about coffee must have:
Name: BRAZIL (the biggest font in that design)
Region: Santos
Altitude: 60 – 1200 m.n.m.
Variety: Arabica
Processing: unwashed

```html
<!DOCTYPE html>
<html lang="en">
<head>
<meta charset="utf-8">
<title>Kestrel Coffee – Brazil Stamp Label</title>
<link rel="stylesheet" href="https://fonts.googleapis.com/css2?family=Alfa+Slab+One&family=Archivo+Black&family=Montserrat:wght@700;800&display=swap">
<style>
  :root {
    --page: #f4f4f6;
    --ink: #000000;
    --paper: #ffffff;
    --pattern-light: #9a9a9a;
    --pattern-dark: #5c5c5c;
  }
  * { box-sizing: border-box; margin: 0; padding: 0; }
  html, body {
    width: 1200px;
    height: 1000px;
    overflow: hidden;
    background: var(--page);
  }
  .canvas {
    position: relative;
    width: 1200px;
    height: 1000px;
  }
  .stamp-label {
    position: absolute;
    left: 373px;
    top: 102px;
    width: 454px;
    height: 795px;
    background: var(--ink);
    color: var(--paper);
    overflow: hidden;
  }
  .pattern-band {
    position: absolute;
    left: 28px;
    top: 24px;
    width: 146px;
    height: 746px;
    border: 3px solid var(--paper);
    background: linear-gradient(180deg, var(--pattern-light), var(--pattern-dark) 50%, var(--pattern-light));
  }
  .brand-mark {
    position: absolute;
    left: 210px;
    top: 20px;
    width: 216px;
    height: 216px;
  }
  .brand-mark svg {
    position: absolute;
    inset: 0;
  }
  .brand-name {
    position: absolute;
    inset: 0;
    display: flex;
    flex-direction: column;
    align-items: center;
    justify-content: center;
    font-family: "Archivo Black", sans-serif;
    color: var(--paper);
    line-height: 1;
    text-align: center;
  }
  .brand-name .word-main { font-size: 31px; letter-spacing: 0.5px; }
  .brand-name .word-sub { font-size: 22px; margin-top: 6px; letter-spacing: 1px; }

  .coffee-info {
    position: absolute;
    left: 424px;
    top: 254px;
    width: 505px;
    height: 220px;
    transform: rotate(90deg);
    transform-origin: top left;
  }
  .origin-name {
    display: flex;
    justify-content: space-between;
    font-family: "Alfa Slab One", serif;
    font-size: 58px;
    line-height: 56px;
    height: 56px;
    color: var(--paper);
  }
  .spec-group {
    position: absolute;
    top: 72px;
    width: 245px;
    border-left: 6px solid var(--paper);
    padding-left: 10px;
    font-family: "Archivo Black", sans-serif;
    line-height: 1;
  }
  .spec-group.origin { left: 0; }
  .spec-group.bean { left: 252px; }
  .spec-label {
    display: block;
    font-family: "Montserrat", sans-serif;
    font-weight: 800;
    font-size: 14px;
    letter-spacing: 0.5px;
    margin-bottom: 2px;
  }
  .spec-value {
    display: block;
    font-size: 33px;
    margin-bottom: 6px;
  }
  .spec-value.large { font-size: 38px; margin-bottom: 2px; }
  .spec-unit {
    display: block;
    font-family: "Montserrat", sans-serif;
    font-weight: 800;
    font-size: 14px;
  }
</style>
</head>
<body>
<main class="canvas">
  <section class="stamp-label">
    <div class="pattern-band" role="img" aria-label="Vertical band of repeating coffee leaf pattern"></div>

    <div class="brand-mark">
      <svg width="216" height="216" viewBox="0 0 216 216" aria-hidden="true">
        <circle cx="108" cy="108" r="101" fill="none" stroke="#ffffff" stroke-width="8"/>
      </svg>
      <div class="brand-name">
        <span class="word-main">KESTREL</span>
        <span class="word-sub">COFFEE</span>
      </div>
    </div>

    <div class="coffee-info">
      <h1 class="origin-name">
        <span>B</span><span>R</span><span>A</span><span>Z</span><span>I</span><span>L</span>
      </h1>
      <div class="spec-group origin">
        <span class="spec-label">REGION</span>
        <span class="spec-value">SANTOS</span>
        <span class="spec-label">ALTITUDE</span>
        <span class="spec-value large">60-1200</span>
        <span class="spec-unit">M.N.M.</span>
      </div>
      <div class="spec-group bean">
        <span class="spec-label">VARIETY</span>
        <span class="spec-value large">ARABICA</span>
        <span class="spec-label">PROCESSING</span>
        <span class="spec-value">UNWASHED</span>
      </div>
    </div>
  </section>
</main>
</body>
</html>
```